Flyer to promote new Commercial HVAC Preventative Maintenance clients

This flyer will be in the body of emails that will be sent to new, existing, and/or potential commericial buildings HVAC clients. It will have the least amount of words used, but it will convey the point with pertinent pictorial and graphics. It will show the value of a Periodic/Preventative routine maintenance to lower operating costs of their commericial buildings (i.e. office, medical, shopping centers, apartment, warehouse facility, etc.), in the following ways:
1) Reduce monthly power usage,
2) Reduce emergency HVAC service calls,
3) Reduce costly repairs costs,
4) Reduce HVAC down-times and angry tenants,
5) Increases the life expectancy of the existing and/or new HVAC equipment in the building and/or the equipment's' early replacement costs,
6) Reduces tenant's early termination of their lease and law suits against the landlords,
7) Increases tenant's renewal of the lease and agree to pay the increase rental rates,
8) Reduces unhappy customers and increases tenant's productivity,
9) By reducing the landlord's expenses, the value of the property will increase considerably and profitable to sell their holdings, or refinance and keep their holdings with an increased ROI (Return On Investment).

Landlords can not depend on their tenants' obligation to maintain the landlords' major assets, which is their HVAC equipment and systems.

With the periodic maintenance done by one reliable and licensed HVAC company, the will not use different companies that may or may not do the right repair job on their unit and hurt their bottom line and increase HVAC replacement COSTLY rates.

```html
<!DOCTYPE html>
<html lang="en">
<head>
<meta charset="utf-8">
<title>HVAC Preventative Maintenance</title>
<link href="https://fonts.googleapis.com/css2?family=Poppins:wght@400;500;600;700;800&display=swap" rel="stylesheet">
<style>
:root{
  --orange:#ef6c0f;
  --ink:#1f1f1f;
  --navy:#173a56;
  --text:#2b2b2b;
  --footer:#3a3a3a;
  --white:#ffffff;
}
*{margin:0;padding:0;box-sizing:border-box}
html,body{width:1200px;height:2210px;overflow:hidden;background:var(--white)}
body{font-family:'Poppins',sans-serif;color:var(--text);position:relative}
.hero{position:absolute;left:0;top:0;width:1200px;height:622px;
  background:linear-gradient(180deg,#b9cfe6 0%,#dfe8f1 45%,#eef1f4 75%,#d9dde1 100%)}
.hero-photo{position:absolute;left:480px;top:0;width:720px;height:622px;
  background:linear-gradient(90deg,rgba(230,234,238,0) 0%,rgba(230,233,236,.7) 25%,rgba(244,245,246,.85) 60%,rgba(207,212,217,.9) 100%)}
.brand{position:absolute;left:75px;top:28px;font-size:30px;font-weight:700;color:var(--ink)}
.hero-title{position:absolute;left:45px;top:160px;font-size:55px;font-weight:800;line-height:72px;color:var(--ink)}
.hero-title span{color:var(--orange)}
.hero-text{position:absolute;left:45px;top:302px;width:440px;font-size:21.5px;line-height:36px;color:#222}
.cta{position:absolute;left:45px;top:437px;width:228px;height:67px;border-radius:34px;background:var(--orange);
  color:var(--white);font-size:25px;font-weight:700;display:flex;align-items:center;justify-content:center}
.section-title{position:absolute;left:0;width:1200px;top:708px;text-align:center;font-size:40px;font-weight:800;color:var(--ink)}
.section-title span{color:var(--orange)}
.service-photo{position:absolute;left:411px;top:793px;width:378px;height:378px;border-radius:50%;
  background:linear-gradient(180deg,#7fb0dc 0%,#b9d3ea 45%,#8a8a84 70%,#a9a08a 100%);
  box-shadow:0 8px 18px rgba(0,0,0,.25)}
.ring{position:absolute;left:0;top:780px}
.benefit{position:absolute;font-size:16px;line-height:28px;color:var(--text)}
.benefit.right-align{text-align:right}
.benefit.compact{font-size:15px;line-height:22px}
.benefit.tight{line-height:21px}
.banner{position:absolute;left:0;top:1549px;width:1200px;height:303px;
  background:linear-gradient(180deg,#e9782a 0%,#ef7a22 50%,#f08a3a 100%);
  display:flex;align-items:center;justify-content:center}
.banner p{width:1170px;text-align:center;color:var(--white);font-size:22.5px;font-weight:600;line-height:43.5px}
.footer{position:absolute;left:0;top:1852px;width:1200px;height:358px;background:var(--footer);color:var(--white)}
.footer-brand{position:absolute;left:0;width:1200px;top:68px;text-align:center;font-size:42px;font-weight:600}
.contact{position:absolute;left:120px;top:155px;width:962px;height:113px;border:1.5px solid var(--white);display:flex}
.contact-item{display:flex;align-items:center;gap:18px;padding-left:30px;border-right:1.5px solid var(--white)}
.contact-item:last-child{border-right:none}
.contact-item:nth-child(1){width:387px}
.contact-item:nth-child(2){width:325px}
.contact-item:nth-child(3){flex:1}
.contact-label{font-size:21px;font-weight:600}
.contact-value{font-size:15px;font-weight:500;line-height:22px}
.copyright{position:absolute;left:0;width:1200px;top:298px;text-align:center;font-size:15.5px;font-weight:500}
</style>
</head>
<body>

<header class="hero">
  <div class="hero-photo" role="img" aria-label="Row of outdoor HVAC condenser units on a rooftop under a blue sky"></div>
  <div class="brand">HVAC</div>
  <h1 class="hero-title">WELCOME TO<br><span>HVAC</span></h1>
  <p class="hero-text">Lorem ipsum dolor sit amet, consectetur adipiscing elit, sed do eiusmod tempor incididunt ut labore et dolore magna.</p>
  <div class="cta">GET STARTED</div>
</header>

<h2 class="section-title">OUR <span>SERVICES</span></h2>

<div class="service-photo" role="img" aria-label="HVAC technician with tool case and gauges on a commercial rooftop"></div>

<svg class="ring" width="1200" height="560" viewBox="0 780 1200 560">
  <path d="M352 961 A228 228 0 0 0 847 969" fill="none" stroke="#e8836a" stroke-width="1.5"/>
  <g fill="var(--white)" stroke="var(--orange)" stroke-width="3">
    <circle cx="352" cy="961" r="10"/><circle cx="364" cy="1042" r="10"/><circle cx="414" cy="1125" r="10"/>
    <circle cx="493" cy="1189" r="10"/><circle cx="607" cy="1209" r="10"/><circle cx="694" cy="1194" r="10"/>
    <circle cx="774" cy="1143" r="10"/><circle cx="840" cy="1035" r="10"/><circle cx="847" cy="969" r="10"/>
  </g>
  <g fill="var(--orange)">
    <circle cx="352" cy="961" r="5"/><circle cx="364" cy="1042" r="5"/><circle cx="414" cy="1125" r="5"/>
    <circle cx="493" cy="1189" r="5"/><circle cx="607" cy="1209" r="5"/><circle cx="694" cy="1194" r="5"/>
    <circle cx="774" cy="1143" r="5"/><circle cx="840" cy="1035" r="5"/><circle cx="847" cy="969" r="5"/>
  </g>
  <g fill="var(--white)" stroke="var(--navy)" stroke-width="3">
    <circle cx="292" cy="942" r="37"/><circle cx="304" cy="1063" r="37"/><circle cx="364" cy="1164" r="37"/>
    <circle cx="466" cy="1243" r="37"/><circle cx="604" cy="1275" r="37"/><circle cx="733" cy="1249" r="37"/>
    <circle cx="835" cy="1155" r="37"/><circle cx="904" cy="1050" r="37"/><circle cx="904" cy="950" r="37"/>
  </g>
  <g fill="none" stroke="var(--orange)" stroke-width="2.5" stroke-linecap="round" stroke-linejoin="round">
    <circle cx="283" cy="936" r="9"/><circle cx="303" cy="944" r="9"/><path d="M278 960h28"/>
    <rect x="287" y="1050" width="34" height="18" rx="2"/><path d="M291 1075v6M303 1075v6M315 1075v6"/>
    <rect x="348" y="1150" width="32" height="28" rx="2"/><path d="M354 1170l7-7 6 5 8-10"/>
    <circle cx="466" cy="1243" r="14"/><path d="M466 1229v28M452 1243h28M456 1233l20 20M476 1233l-20 20"/>
    <rect x="588" y="1272" width="32" height="14" rx="2"/><path d="M596 1262v-6M612 1262v-6M592 1292h24"/>
    <path d="M724 1236v24M720 1255l4 5 4-5M742 1262v-24M738 1243l4-5 4 5"/>
    <rect x="822" y="1140" width="26" height="18" rx="2"/><path d="M826 1166h18M829 1149l3 3 6-6"/>
    <circle cx="904" cy="1050" r="16"/><path d="M897 1058q7-6 14 0M898 1044h4M906 1044h4"/>
    <path d="M891 964l12-14 6 6 10-14M889 964h30M914 942h5v5"/>
  </g>
</svg>

<p class="benefit right-align" style="left:40px;top:915px;width:202px">Reduce monthly power usage,</p>
<p class="benefit right-align" style="left:40px;top:1035px;width:215px">Reduce emergency HVAC service calls,</p>
<p class="benefit right-align" style="left:40px;top:1160px;width:265px">Reduce costly repairs costs,</p>
<p class="benefit right-align tight" style="left:100px;top:1240px;width:310px">Reduce HVAC down-times and angry tenants,</p>
<p class="benefit" style="left:432px;top:1322px;width:355px;text-align:center">Increases the life expectancy of the existing and/or new HVAC equipment in the building and/or the equipment's' early replacement costs,</p>
<p class="benefit" style="left:797px;top:1226px;width:300px">Reduces tenant's early termination of their lease and law suits against the landlords,</p>
<p class="benefit compact" style="left:894px;top:1130px;width:270px">Increases tenant's renewal of the lease and agree to pay the increase rental rates,</p>
<p class="benefit compact" style="left:960px;top:1022px;width:215px">Reduces unhappy customers and increases tenant's productivity,</p>
<p class="benefit compact" style="left:963px;top:910px;width:220px">or refinance and keep their holdings with an increased ROI (Return On</p>
<p class="benefit compact" style="left:872px;top:794px;width:295px">By reducing the landlord's expenses, the value of the property will increase considerably and it is profitable to sell their holdings, Investment).</p>

<section class="banner" role="img" aria-label="Residential AC condenser units beside a house, tinted orange">
  <p>Landlords can not depend on their tenants' obligation to maintain the landlords' major assets, which is their HVAC equipment and systems.With the periodic maintenance done by one reliable and licensed HVAC company, the will not use different companies that may or may not do the right repair job on their unit and hurt their bottom line and increase HVAC replacement COSTLY rates.</p>
</section>

<footer class="footer">
  <div class="footer-brand">HVAC</div>
  <div class="contact">
    <div class="contact-item">
      <svg width="52" height="60" viewBox="0 0 52 60" fill="none" stroke="#fff" stroke-width="3" stroke-linejoin="round">
        <path d="M26 44C16 32 12 26 12 19a14 14 0 0 1 28 0c0 7-4 13-14 25z"/><circle cx="26" cy="19" r="6"/>
        <path d="M16 40L3 50l23 8 23-8-13-10"/>
      </svg>
      <div><div class="contact-label">Location :</div><div class="contact-value">3175 HVAC<br>Suite 330 Lorem ipsum dolor , 89052</div></div>
    </div>
    <div class="contact-item">
      <svg width="50" height="50" viewBox="0 0 50 50" fill="none" stroke="#fff" stroke-width="3" stroke-linejoin="round">
        <path d="M4 20l21-15 21 15v26H4z"/><path d="M4 20l21 15 21-15"/><path d="M4 46l16-14M46 46L30 32"/>
        <circle cx="25" cy="19" r="5"/>
      </svg>
      <div><div class="contact-label">Email :</div><div class="contact-value">info@airkeep.com</div></div>
    </div>
    <div class="contact-item">
      <svg width="54" height="54" viewBox="0 0 54 54" fill="none" stroke="#fff" stroke-width="3">
        <circle cx="27" cy="27" r="24"/>
        <path d="M18 14l6 7-3 4c2 4 5 7 9 9l4-3 7 6-4 5c-10-1-21-12-22-22z" stroke-linejoin="round"/>
      </svg>
      <div><div class="contact-label">Phone :</div><div class="contact-value">+1 555 014 2290</div></div>
    </div>
  </div>
  <div class="copyright">© 2023 HVAC | All Rights Reserved</div>
</footer>

</body>
</html>
```